Brochure for a civil enineering company in A4 format

I need a brochure design for our company VELTA Engineering S.r.l.. We are an engineering consultant company. Our main clients are from the infrastructure industry (geotechnical and underground sectors mainly).
We are looking for a 2 pages (4 faces) fold out design with a glued pocket where we can put individual data sheets.
I need A4 format pages.

Target Market(s)

We are an engineering consultant company. Our main clients are from the infrastructure industry (geotechnical and underground sectors mainly).

Industry/Entity Type

Civil Engineer

Font styles to use
Sans Serif

Requirements
Must have
• Overall: 2 pages in A4 format
Essential style. Bright and modern appearance.
Glued pocket
Logo integrated in a picture on the pocket where I would like to insert a slogan (… velta engineering … reliable solutions …)
Attached are selected images which the designer can use and edit at their own discretion.
Some advice in the following (anyway designers are free to provide their solutions):
Outer sheets:
Front page with name, logo. It could be nice to have the “m” of the logo integrated in a pictures, also a modified picture (I mean modify one of the attached pictures) so to create a general image and do not tie the cover to a specific job.
Back page: offices address and contact email address. Nice to have one space for a slogan.
Inner sheet: text that I upload in the file “inside-sheets”, possibly with pictures on each sheet. In the right faces insert the glued pocket. On this pages insert the section OUR EXPERIENCE ….with a space for a picture of our team.
Nice to have
• Clean and essential design.
Pictures choosing from the atteched ones. Pictures could be modified in a very light manner to make them a general idea of the work ( I mean geotechnical world) without to be immediately linked to a specific site.
Should not have
• excessive frills

```html
<!DOCTYPE html>
<html lang="it">
<head>
<meta charset="utf-8">
<title>VELTA Engineering – Brochure</title>
<link href="https://fonts.googleapis.com/css2?family=Inter:wght@400;500;600&family=IBM+Plex+Mono:wght@400&display=swap" rel="stylesheet">
<style>
:root{
  --bg:#dedede;
  --paper:#ffffff;
  --ink:#1d1d1d;
  --text:#3a3a3a;
  --wave-1:#ecedee;
  --wave-2:#dfe0e2;
  --wave-3:#d0d2d5;
  --wave-4:#c2c4c8;
  --avatar:#b9bbbe;
}
*{box-sizing:border-box;margin:0;padding:0}
html,body{width:824px;height:1200px;overflow:hidden;background:var(--bg)}
body{font-family:"Inter",Arial,sans-serif;color:var(--text);position:relative}
.sheet-set{position:absolute;left:16px;top:225px;width:1415px;height:1340px;transform:scale(.56);transform-origin:0 0}
.spread{position:absolute;left:0;width:1415px;height:667px;background:var(--paper);overflow:hidden}
.spread--outer{top:0}
.spread--inner{top:673px}
.photo-strip{position:absolute;left:0;width:100%;display:flex}
.photo-strip .photo{flex:1;height:100%}
.spread--outer .photo-strip{top:333px;height:150px}
.spread--inner .photo-strip{top:0;height:157px}
.waves{position:absolute;left:0;width:100%}
.tagline{position:absolute;right:113px;top:75px;font-family:"IBM Plex Mono",monospace;font-size:9.5px;letter-spacing:2.6px;color:var(--ink)}
.brand{position:absolute;font-family:"Inter",Arial,sans-serif;font-weight:500;color:var(--ink);letter-spacing:-.5px;line-height:1}
.brand--cover{left:1122px;top:193px;font-size:40px}
.brand--inner{left:682px;top:616px;font-size:20px}
.contacts{position:absolute;left:150px;top:155px;width:175px;text-align:center;font-size:8.5px;line-height:10px;color:var(--ink)}
.contacts .office{margin-bottom:7px}
.contacts strong{font-weight:600}
.web{position:absolute;right:180px;top:630px;font-size:9px;color:#444}
.column{position:absolute;top:176px;font-size:7.6px;line-height:9.4px;text-align:justify}
.column--company{left:55px;width:365px}
.column--team{left:524px;width:366px}
.column h2{font-size:11px;font-weight:500;color:var(--ink);margin-bottom:3px;letter-spacing:.1px}
.column p{margin-bottom:4px}
.column h2+p{margin-top:0}
.services{list-style:none;padding-left:12px}
.services li{position:relative;margin-bottom:4px;padding-left:6px}
.services li::before{content:"•";position:absolute;left:-3px}
.member{overflow:hidden;margin-bottom:9px}
.avatar{float:left;width:42px;height:42px;border-radius:50%;background:var(--avatar);margin:3px 6px 2px 0}
</style>
</head>
<body>
<main class="sheet-set">

  <section class="spread spread--outer" aria-label="Pagine esterne: retro e copertina">
    <div class="contacts">
      <div class="office"><strong>Milano</strong><br>Via Verdi, 14<br>20121 Milano - IT<br>+39 02 4455 6677</div>
      <div class="office"><strong>Riva TN</strong><br>Via Garibaldi, 12<br>38066 Riva TN - IT<br>+39 02 4455 6677</div>
      <div>www.veltaengineering.org<br>info@veltaengineering.org</div>
    </div>
    <p class="tagline">PIÙ INGEGNERIA , SOLUZIONI AFFIDABILI</p>
    <div class="brand brand--cover">velta</div>

    <div class="photo-strip">
      <div class="photo" role="img" aria-label="Foto: galleria illuminata in costruzione" style="background:linear-gradient(160deg,#6b625a,#c9c2b6 55%,#7d7367)"></div>
      <div class="photo" role="img" aria-label="Foto: scavo con travi in calcestruzzo" style="background:linear-gradient(180deg,#c7ccd2 0,#8c8a78 40%,#5d5b54)"></div>
      <div class="photo" role="img" aria-label="Foto: interno di galleria in notturna" style="background:linear-gradient(160deg,#3b3f5a,#8a8aa8 55%,#2d2e40)"></div>
      <div class="photo" role="img" aria-label="Foto: cantiere urbano con scavo" style="background:linear-gradient(180deg,#b9c4d0 0,#a28e7c 40%,#cfcac2)"></div>
      <div class="photo" role="img" aria-label="Foto: galleria con centine in bianco e nero" style="background:linear-gradient(160deg,#1f1f1f,#9a9a9a 55%,#2a2a2a)"></div>
      <div class="photo" role="img" aria-label="Foto: vista aerea di area di cantiere" style="background:linear-gradient(180deg,#8d9a80,#b8b2a5 50%,#6f7560)"></div>
      <div class="photo" role="img" aria-label="Foto: pozzo con armature" style="background:linear-gradient(160deg,#4c4336,#a99a83 50%,#5a5044)"></div>
      <div class="photo" role="img" aria-label="Foto: imbocchi di galleria con gru" style="background:linear-gradient(180deg,#c6d0da 0,#a49a88 40%,#6c6456)"></div>
      <div class="photo" role="img" aria-label="Foto: galleria con rivestimento" style="background:linear-gradient(160deg,#3b342e,#b4ab9f 55%,#4a4038)"></div>
    </div>

    <svg class="waves" style="top:440px;height:227px" viewBox="0 0 1415 227" preserveAspectRatio="none" aria-hidden="true">
      <path d="M0 30 C180 10 360 40 600 30 C850 20 1100 5 1415 35 V227 H0Z" fill="var(--wave-1)"/>
      <path d="M0 55 C250 60 500 40 750 60 C1000 80 1200 45 1415 60 V227 H0Z" fill="var(--wave-2)"/>
      <path d="M0 120 C200 105 450 130 700 115 C950 100 1200 130 1415 110 V227 H0Z" fill="var(--wave-3)"/>
      <path d="M0 170 C250 160 500 180 750 165 C1000 150 1250 170 1415 160 V227 H0Z" fill="var(--wave-4)"/>
    </svg>
    <p class="web">www.veltaengineering.org</p>
  </section>

  <section class="spread spread--inner" aria-label="Pagine interne">
    <div class="photo-strip">
      <div class="photo" role="img" aria-label="Foto: interno di stazione in costruzione" style="background:linear-gradient(160deg,#6e6456,#b3a892 55%,#5b5245)"></div>
      <div class="photo" role="img" aria-label="Foto: gru che solleva testa di fresa" style="background:linear-gradient(180deg,#5e86b8,#b8c6d2 45%,#9e6a55)"></div>
      <div class="photo" role="img" aria-label="Foto: escavatore in galleria" style="background:linear-gradient(160deg,#3a2f27,#8d7a68 50%,#b06a36)"></div>
      <div class="photo" role="img" aria-label="Foto: cantiere davanti a edificio storico" style="background:linear-gradient(180deg,#c9d3dd,#b9ab98 45%,#6a625a)"></div>
      <div class="photo" role="img" aria-label="Foto: scavo sotto solaio" style="background:linear-gradient(180deg,#cfcfcf,#4a443d 40%,#2f2a25)"></div>
      <div class="photo" role="img" aria-label="Foto: scavo urbano con armature" style="background:linear-gradient(180deg,#c5ccd4,#a99784 45%,#d8d2ca)"></div>
      <div class="photo" role="img" aria-label="Foto: pozzo circolare con macchinari" style="background:linear-gradient(160deg,#5a5a4e,#aaa590 50%,#4a4a40)"></div>
      <div class="photo" role="img" aria-label="Foto: viadotto in valle montana" style="background:linear-gradient(180deg,#b7c8da,#7d8a80 55%,#8a6e58)"></div>
      <div class="photo" role="img" aria-label="Foto: scavo con imbocco e armature" style="background:linear-gradient(160deg,#6a5e50,#bfb5a6 50%,#5f554a)"></div>
    </div>

    <svg class="waves" style="top:380px;height:287px" viewBox="0 0 1415 287" preserveAspectRatio="none" aria-hidden="true">
      <path d="M0 25 C200 5 420 35 650 25 C900 15 1150 0 1415 20 V287 H0Z" fill="var(--wave-1)"/>
      <path d="M0 95 C250 100 500 80 750 95 C1000 110 1200 85 1415 95 V287 H0Z" fill="var(--wave-2)"/>
      <path d="M0 170 C200 160 450 180 700 168 C950 156 1200 178 1415 165 V287 H0Z" fill="var(--wave-3)"/>
      <path d="M0 230 C250 222 500 240 750 228 C1000 216 1250 235 1415 225 V287 H0Z" fill="var(--wave-4)"/>
    </svg>

    <div class="column column--company">
      <h2>LA NOSTRA AZIENDA</h2>
      <p>VELTA Engineering S.r.l. offre servizi di consulenza tecnica, contrattuale e strategica ai principali attori nei settori delle scienze geologiche, dell'ingegneria geotecnica e dell'ingegneria idraulica. Lavoriamo per mitigare il rischio e ridurre l'incertezza, con flessibilità nella ricerca della soluzione ottimale contribuendo ad aumentare la redditività del progetto. VELTA Engineering S.r.l. è una società indipendente che nasce nel luglio 2020 dall'associazione di un gruppo di professionisti che hanno messo a fattor comune la reciproca esperienza maturata in oltre trent'anni di attività come progettisti e consulenti nel settore delle grandi opere di ingegneria civile.</p>
      <p>VELTA Engineering S.r.l. vuole unire l'esperienza dei Fondatori e delle figure chiave con l'entusiasmo di chi intraprende una nuova attività, per dare vita ad una nuova realtà che si pone come obiettivo principale il design di infrastrutture sicure, sostenibili ed economiche.</p>
      <p>Ciascuno dei nostri progetti rappresenta un impegno a lungo termine, crediamo nel fornire sicurezza, affidabilità, soluzioni innovative e sostenibili. Questa è e sarà la nostra caratteristica distintiva.</p>
      <h2>I NOSTRI SERVIZI</h2>
      <p>Progettazione e consulenza specialistica nel campo della geologia, dell'ingegneria geotecnica, delle opere sotterranee e dell'ingegneria idraulica.</p>
      <p>Aiutiamo i nostri clienti a risolvere problemi di natura progettuale, contrattuale e costruttiva che possono nascere nell'intera vita del progetto portando la nostra esperienza all'interno delle loro organizzazioni, migliorando la qualità dei loro servizi di ingegneria, ottimizzando i loro progetti, proponendo nuove idee e soluzioni.</p>
      <p>VELTA Engineering è in grado di fornire la propria assistenza nell'intero iter procedurale, dalla fase di indagine preliminare e di analisi di fattibilità fino alla progettazione costruttiva e all'assistenza tecnica in fase realizzativa.</p>
      <p>La specializzazione e l'esperienza accumulate nelle discipline della geologia, dell'ingegneria geotecnica e del sottosuolo e dell'idraulica ci permette di massimizzare la nostra efficacia quando sia necessario:</p>
      <ul class="services">
        <li>far fronte a situazioni di emergenza anche su progetti in fase di sviluppo avanzato garantendo l'immediata focalizzazione delle problematiche di progetto e garantendo il risultato finale atteso (in termini di qualità, tempistiche e costi…)</li>
        <li>fornire "second opinion" di elevato valore tecnico ed amministrativo in occasione di problematiche progettuali e costruttive e dispute legali</li>
        <li>analizzare in tempi brevi progetti svolti da terzi individuandone le "criticità", verificandone la cantierabilità e la validità tecnico economica.</li>
        <li>ottimizzare i progetti redatti da terzi implementandone il contenuto e massimizzando l'efficacia economica degli investimenti.</li>
      </ul>
    </div>

    <div class="column column--team">
      <h2>LA NOSTRA COMPETENZA ED ESPERIENZA</h2>
      <p>La società nasce dall'associazione di un gruppo di professionisti, con indiscusse competenze ed affidabilità, con esperienza maturata in oltre trent'anni di attività come progettisti e consulenti nel settore delle grandi opere di ingegneria civile; geologia, ingegneria geotecnica ed idraulica ed opere sotterranee sono il "core" delle loro competenze ….</p>
      <p>I soci fondatori sono:</p>
      <div class="member"><div class="avatar" role="img" aria-label="Spazio per ritratto del socio"></div><p>Marco. Già Direttore Tecnico e Socio di NORDA Srl, nel periodo di sua permanenza fino al dicembre 2018, ha per essa firmato tutti i progetti nel campo delle opere sotterranee e la maggior parte di quelli di ingegneria geotecnica. Da gennaio 2019 è Direttore Tecnico di GTEC. Può vantare più di 150 gallerie naturali, e numerosi progetti ed assistenze tecniche nel campo delle strutture geotecniche, delle sistemazioni idrogeologiche e dei versanti e delle opere di protezione ambientale. Negli ultimi dieci anni è stato responsabile di attività di assistenza tecnica, per imprese di costruzione, di opere il cui valore supera i 440 Mio EUR e di servizi di progettazione definitiva o esecutiva per opere il cui valore supera i 1.400 Mio EUR. Ha svolto attività di verifica e validazione, in Italia ed all'estero, di numerosi progetti il cui valore complessivo supera i 3.400 Mio EUR.</p></div>
      <div class="member"><div class="avatar" role="img" aria-label="Spazio per ritratto del socio"></div><p>Paolo 30 anni di esperienza professionale. Coinvolto in più di 150 gallerie naturali con lunghezza complessiva superiore a 360 km. Numerosi progetti ed attività di assistenza tecnica nel campo delle strutture, delle sistemazioni idrogeologiche e dei versanti e delle opere di protezione ambientale. Negli ultimi dieci anni responsabile di attività di assistenza tecnica in corso d'opera, per imprese di costruzione, di opere il cui valore supera i 440 Mio EUR e di servizi di progettazione definitiva o esecutiva per opere il cui valore supera i 1.400 Mio EUR. Ha svolto attività di verifica ai fini della validazione, in Italia ed all'estero, di numerosi progetti il cui valore complessivo supera i 3.400 Mio EUR.</p></div>
      <div class="member"><div class="avatar" role="img" aria-label="Spazio per ritratto della socia"></div><p>Giulia 30 anni di esperienza professionale. Coinvolta in più di 150 gallerie naturali con lunghezza complessiva superiore a 360 km. Numerosi progetti ed attività di assistenza tecnica nel campo delle strutture, delle sistemazioni idrogeologiche e dei versanti e delle opere di protezione ambientale. Negli ultimi dieci anni responsabile di attività di assistenza tecnica in corso d'opera, per imprese di costruzione, di opere il cui valore supera i 440 Mio EUR e di servizi di progettazione definitiva o esecutiva per opere il cui valore supera i 1.400 Mio EUR. Ha svolto attività di verifica ai fini della validazione, in Italia ed all'estero, di numerosi progetti il cui valore complessivo supera i 3.400 Mio EUR.</p></div>
      <div class="member"><div class="avatar" role="img" aria-label="Spazio per ritratto della socia"></div><p>Chiara 30 anni di esperienza professionale. Coinvolta in più di 150 gallerie naturali con lunghezza complessiva superiore a 360 km. Numerosi progetti ed attività di assistenza tecnica nel campo delle strutture, delle sistemazioni idrogeologiche e dei versanti e delle opere di protezione ambientale. Negli ultimi dieci anni responsabile di attività di assistenza tecnica in corso d'opera, per imprese di costruzione, di opere il cui valore supera i 440 Mio EUR e di servizi di progettazione definitiva o esecutiva per opere il cui valore supera i 1.400 Mio EUR. Ha svolto attività di verifica ai fini della validazione, in Italia ed all'estero, di numerosi progetti il cui valore complessivo supera i 3.400 Mio EUR.</p></div>
    </div>

    <div class="brand brand--inner">velta</div>
  </section>

</main>
</body>
</html>
```